Vacation/Holiday Home Wordpress Website

I currently have a website for our vacation/holiday rental home. It is 6 years old and needs a complete redesign to acommodate many new features available today. The existing website can be seen at www.coralwindstays.co.uk . The purpose of the website is mainly to provide useful infomation about our home, the destination of Barbados. The customer is also able to check availability and book. Please note that there is a booking element to the website which is hosted externally. This can be seen at

http://stay.reservequick-hub.net/PickArrival_Mini.asp?ref=kTR%3DWQPA%26LMN%3DHXJX

I now wish to add key functionality such as:

- Video of property and area
- Customer video testimonials
- Other useful information

The navigation, menus and buttons need to be re designed to give a modern, innovative and professional look and feel.

My customers are mainly females between the ages of 35 and 55. The website needs to reassure customers who are parting with a lot of mony by booking online. It needs to give a sense of trust as this may be a once in a lifetime trip which they have saved up for for a long time. Many visitors to the website will be referred by other websites such as www.nestroam.co.uk and www.villaquarters.co.uk.
Updates

Dear designers, 

Thank you for taking the time to write some further comments to you all. 

1. The homepage should have an availability search function as a key feature

2. The look and feel does NOT need to have the 3 feature columns like my current website has

3.  There should not be too much text on the homepage. Brief text can be included with 'more'  buttons to reveal more information 

4.  For designs that are under consideration, we will need to see a design for the other pages as they will be different to the homepage. Information from other pages on the existing website can be used. 

Reason: Dear all, I will be providing extensive feedback later today following a review that we have conducted with a group of our guests. To enable you to read and use this information, we have extended the deadline by 5 days. Thank you for the design submisions so far. We hope that the additional feedback will enable you to amend your designs appropriately. Regards Martin Elswick

Dear all,

Thank you for your designs.  I apologise that I am unable to give detailed feedback on each and every design submitted.  I will contact you individually and indicate whether we would like you to submit any further designs.  These should take into account the feedback below.

Feedback from design review group

1.  Logo should not be displayed in a white box.  It should blend in with the background or be overlayed onto the picture.

2.  There must be an availability calendar on the home page.

3.  Any background image should be subtle, maybe blurred and not distract from the main area.

4.  Text should be limited to a few key words with a 'read more' button to reveal more information.

5.  A gallery/slide show should be featured in the top part of the screen

6.  Icons can be used as navigation buttons

7.  Video testimonials is a key feature and should appear on the home page

8.   The use of bold and vibrant colours is preferred

9.   The 3 column format of the old website should not be copied

Regards

Martin

Target Market(s)

Female's, Families, 35 to 55 year olds, travellers to Barbados

Industry/Entity Type

Online

Requirements
Must have
• Pictures
Video
Testimonials
Clear and stylish navigation
Easy to use navigation
Should not have
• Dated look or feel

```html
<!DOCTYPE html>
<html lang="en">
<head>
<meta charset="utf-8">
<title>Coral Wind Stays – Corallo Holiday Home</title>
<link rel="stylesheet" href="https://fonts.googleapis.com/css2?family=Ubuntu:wght@400;500;700&family=Satisfy&display=swap">
<style>
:root{
  --blue:#0a6cc4;
  --blue-dark:#0558a8;
  --blue-light:#1a86dc;
  --red:#e8260f;
  --red-dark:#c81a06;
  --text:#1b1b1b;
  --muted:#666;
  --panel:#ffffff;
  --tab:#2b2b2b;
  --sky-top:#c9d3de;
}
*{box-sizing:border-box;margin:0;padding:0}
html,body{width:1200px;height:1135px;overflow:hidden}
body{font-family:"Ubuntu",sans-serif;color:var(--text);position:relative;background:#fff}
.backdrop{position:absolute;left:0;top:0;width:1200px;height:640px;
  background:linear-gradient(180deg,var(--sky-top) 0%,#d9dfe6 40%,#e6e9ec 75%,#fff 100%)}
.page{position:absolute;left:117px;top:0;width:967px}

/* header */
.brand{position:absolute;left:0;top:52px;display:flex;align-items:center;gap:8px}
.brand-dot{width:14px;height:14px;border-radius:50%;background:var(--red);flex:none}
.brand-name{font-size:20px;font-weight:500;color:var(--red);letter-spacing:2px}
.social{position:absolute;display:flex;gap:2px}
.social-top{right:0;top:0}
.social a{display:flex;align-items:center;justify-content:center;width:25px;height:29px;background:var(--tab);border-radius:0 0 12px 12px}
.social .mark{width:8px;height:8px;border-radius:50%;background:#fff}
.phone{position:absolute;right:0;top:53px;display:flex;align-items:center;gap:8px;color:var(--blue);font-size:27px}

/* nav */
.nav{position:absolute;left:0;top:117px;width:967px;height:75px}
.nav ul{list-style:none;display:flex;position:absolute;top:33px;left:0;height:42px;width:967px;
  background:linear-gradient(180deg,var(--blue-light),var(--blue-dark))}
.nav li{position:relative;display:flex;align-items:center;justify-content:center;color:#fff;font-size:16px;white-space:nowrap;border-right:1px solid rgba(255,255,255,.12)}
.nav li:last-child{border-right:0}
.nav li.active{background:var(--red)}
.nav-icon{position:absolute;top:-33px;left:50%;margin-left:-21px;width:42px;height:42px;border-radius:50%;background:#fff;border:2px solid var(--blue);display:flex;align-items:center;justify-content:center}
.nav li.active .nav-icon{border-color:var(--red)}
.nav-icon span{width:28px;height:28px;border-radius:50%}

/* hero */
.hero{position:absolute;left:0;top:192px;width:967px;height:391px;display:flex;box-shadow:0 6px 10px -6px rgba(0,0,0,.35)}
.search{width:283px;flex:none;background:var(--panel);padding:0 30px}
.search h2{margin-top:50px;font-size:25px;font-weight:500;color:var(--blue);padding-bottom:9px;border-bottom:3px solid var(--blue);width:218px;white-space:nowrap;letter-spacing:-.4px}
.search label{display:block;font-size:15px;margin:22px 0 9px 1px}
.search label.second{margin-top:14px}
.row{display:flex;gap:6px}
.select{position:relative;height:27px;border:1px solid #c8c8c8;background:#fff;color:#999;font-size:14px;padding:4px 8px}
.select::after{content:"";position:absolute;right:0;top:-1px;bottom:-1px;width:21px;background:#8a8a8a}
.select::before{content:"";position:absolute;right:6px;top:11px;border:4px solid transparent;border-top-color:#fff;z-index:1}
.btn-search{display:block;margin-top:20px;width:217px;height:45px;background:linear-gradient(180deg,#f23a18,var(--red-dark));border:1px solid #a81404;border-radius:2px;color:#fff;font-size:19px;font-weight:700;text-align:center;line-height:43px}
.advanced{display:block;text-align:right;margin-top:11px;color:var(--red);font-size:12px;width:217px}
.slider{position:relative;width:684px;background:linear-gradient(120deg,#d8c29a 0%,#efe4c9 35%,#f6f2e6 55%,#9cc07a 80%,#6e9a4e 100%)}
.slider-arrow{position:absolute;top:150px;width:24px;height:42px;background:#1a1a1a;display:flex;align-items:center;justify-content:center}
.slider-arrow.prev{left:0;border-radius:0 21px 21px 0}
.slider-arrow.next{right:0;border-radius:21px 0 0 21px}
.dots{position:absolute;right:26px;top:314px;display:flex;gap:3px}
.dots i{width:11px;height:11px;border-radius:50%;background:#fff}
.caption{position:absolute;left:0;bottom:0;width:100%;height:50px;background:rgba(40,40,40,.72);color:#fff;font-size:21px;font-weight:700;letter-spacing:-.5px;display:flex;align-items:center;padding-left:20px;gap:6px;white-space:nowrap}

/* content */
.content{position:absolute;left:0;top:602px;width:967px;height:401px;background:#fff;box-shadow:0 0 3px rgba(0,0,0,.15)}
.about-title{position:absolute;left:285px;top:38px;width:400px;height:44px;
  background:linear-gradient(90deg,rgba(185,212,235,0),#cfe0ef 20%,#d7e6f2 80%,rgba(185,212,235,0));
  text-align:center;font-family:"Satisfy",cursive;font-weight:400;font-size:28px;color:var(--blue);line-height:44px}
.about-text{position:absolute;left:60px;top:96px;width:847px;text-align:center;font-size:14px;line-height:16.5px}
.about-text a{color:var(--red);font-size:12px}
.tile{position:absolute;top:173px;width:292px;height:182px;overflow:hidden}
.tile-video{left:25px;background:linear-gradient(180deg,#d9b98a 0%,#b69a7e 35%,#4b6f8a 60%,#2e4f6a 100%)}
.tile-testi{left:338px;background:linear-gradient(180deg,#7fb6d0 0%,#bfd9e2 40%,#d8e4e6 70%,#c9d2d5 100%)}
.play{position:absolute;left:50%;top:66px;margin-left:-26px;width:52px;height:52px;border-radius:50%;background:#1d1d1d;display:flex;align-items:center;justify-content:center}
.play span{width:40px;height:40px;border-radius:50%;background:#fff;display:flex;align-items:center;justify-content:center}
.tile-label{position:absolute;left:0;bottom:0;width:100%;height:34px;background:rgba(60,60,60,.7);color:#fff;font-size:21px;padding-left:11px;line-height:36px}
.calendar{position:absolute;left:650px;top:173px;width:292px;height:182px;background:linear-gradient(180deg,#1e3b4c,#3c5868 45%,#6b7f86 100%);color:#fff}
.cal-head{height:27px;display:flex;justify-content:space-between;align-items:center;padding:0 8px 0 12px;font-size:12px;background:rgba(0,20,35,.55)}
.calendar table{width:100%;border-collapse:collapse;font-size:12px;font-weight:500}
.calendar th,.calendar td{height:25.5px;text-align:center;border-bottom:1px solid rgba(255,255,255,.12)}
.calendar th{background:rgba(0,0,0,.35);height:25px}
.calendar .today span{display:inline-block;width:20px;height:20px;border-radius:50%;background:#222;line-height:20px}

/* footer */
.footer{position:absolute;left:0;top:1030px;width:967px;height:60px}
.footer .brand{top:6px;left:-3px;width:140px}
.footer .brand-name{font-size:13px;letter-spacing:1.5px;line-height:16px;width:100px}
.footer .brand-dot{width:10px;height:10px}
.footer-links{position:absolute;left:162px;top:8px;font-size:12px;color:#555;line-height:19px;white-space:nowrap}
.footer-links .sep{color:#aaa;margin:0 3px}
.footer-rule{position:absolute;left:745px;top:10px;width:225px;height:1px;background:linear-gradient(90deg,rgba(0,0,0,0),#333 30%,#333 70%,rgba(0,0,0,0))}
.social-foot{left:804px;top:11px}
.social-foot a{width:25px;height:32px}
</style>
</head>
<body>
<div class="backdrop" role="img" aria-label="Soft blurred beach scene with palm trees and parasols"></div>

<div class="page">
  <header>
    <div class="brand"><span class="brand-dot"></span><span class="brand-name">CORAL WIND STAYS</span></div>
    <nav class="social social-top" aria-label="Social links">
      <a href="#"><span class="mark"></span></a>
      <a href="#"><span class="mark"></span></a>
      <a href="#"><span class="mark"></span></a>
      <a href="#"><svg width="12" height="9" viewBox="0 0 12 9"><rect x=".5" y=".5" width="11" height="8" fill="none" stroke="#fff"/><path d="M.5 .5 6 5 11.5 .5" fill="none" stroke="#fff"/></svg></a>
    </nav>
    <div class="phone">
      <svg width="16" height="22" viewBox="0 0 16 22"><path d="M4 1 7 6 5 8c1 3 2 6 4 8l2-1 4 4-3 2C5 19 1 11 1 4z" fill="var(--blue)"/></svg>
      0800 555 0192
    </div>
  </header>

  <nav class="nav" aria-label="Main">
    <ul>
      <li style="width:112px"><span class="nav-icon"><span role="img" aria-label="Home icon" style="background:#f2a23a"></span></span>Home</li>
      <li class="active" style="width:221px"><span class="nav-icon"><span role="img" aria-label="Beach chair icon" style="background:#6fb6e0"></span></span>Corallo Holiday Home</li>
      <li style="width:126px"><span class="nav-icon"><span role="img" aria-label="Starfish icon" style="background:#f5c430"></span></span>Local Area</li>
      <li style="width:122px"><span class="nav-icon"><span role="img" aria-label="Luggage icon" style="background:#d99640"></span></span>Book Now</li>
      <li style="width:93px"><span class="nav-icon"><span role="img" aria-label="Payment card icon" style="background:#4a92d0"></span></span>Prices</li>
      <li style="width:144px"><span class="nav-icon"><span role="img" aria-label="Guest note icon" style="background:#e8d6a8"></span></span>Testimonials</li>
      <li style="width:149px"><span class="nav-icon"><span role="img" aria-label="Island icon" style="background:#48b4d8"></span></span>Contact us</li>
    </ul>
  </nav>

  <section class="hero">
    <form class="search">
      <h2>Availability Search</h2>
      <label>Arival Date</label>
      <div class="row">
        <div class="select" style="width:66px">16</div>
        <div class="select" style="width:66px">Aug</div>
        <div class="select" style="width:74px">2013</div>
      </div>
      <label class="second">Length of Stay</label>
      <div class="row">
        <div class="select" style="width:105px">05 Nights</div>
        <div class="select" style="width:105px">04 Days</div>
      </div>
      <span class="btn-search">Search Now</span>
      <a class="advanced">Advanced Search&gt;&gt;</a>
    </form>
    <div class="slider" role="img" aria-label="Bright bedroom with a white double bed, yellow cushions, wicker headboard and a window onto the garden">
      <span class="slider-arrow prev"><svg width="8" height="10" viewBox="0 0 8 10"><path d="M6 1 2 5l4 4" stroke="#fff" stroke-width="2" fill="none"/></svg></span>
      <span class="slider-arrow next"><svg width="8" height="10" viewBox="0 0 8 10"><path d="M2 1l4 4-4 4" stroke="#fff" stroke-width="2" fill="none"/></svg></span>
      <div class="dots"><i></i><i></i><i></i></div>
      <div class="caption">Corallo - Stunning Home Close to Miami / Enterprise Beach!
        <svg width="17" height="17" viewBox="0 0 17 17"><circle cx="8.5" cy="8.5" r="8.5" fill="#fff"/><path d="M7 4.5 11 8.5 7 12.5" stroke="#333" stroke-width="2.4" fill="none"/></svg>
      </div>
    </div>
  </section>

  <section class="content">
    <h2 class="about-title">About Barbados</h2>
    <p class="about-text">Lorem ipsum dolor sit amet, consectetur adipisicing elit, sed do eiusmod tempor incididunt ut labore et dolore magna aliqua. Ut enim ad minim veniam, quis nostrud exercitation ullamco laboris nisi ut aliquip ex ea commodo consequat. Lorem ipsum dolor sit amet, consectetur adipisicing elit, sed do eiusmod tempor incididunt ut labore et dolore magna <a>Learn More &gt;&gt;</a></p>

    <div class="tile tile-video" role="img" aria-label="Couple at the seafront at sunset">
      <span class="play"><span><svg width="14" height="16" viewBox="0 0 14 16"><path d="M1 0 14 8 1 16z" fill="#1d1d1d"/></svg></span></span>
      <div class="tile-label">Our Video</div>
    </div>
    <div class="tile tile-testi" role="img" aria-label="Guests relaxing in white beach chairs by the sea">
      <span class="play"><span><svg width="14" height="16" viewBox="0 0 14 16"><path d="M1 0 14 8 1 16z" fill="#1d1d1d"/></svg></span></span>
      <div class="tile-label">Guest Testimonials</div>
    </div>

    <div class="calendar" role="group" aria-label="Availability calendar">
      <div class="cal-head">AUGUST – 2013
        <svg width="18" height="16" viewBox="0 0 18 16"><rect x=".5" y="2" width="17" height="13.5" fill="#cfd6db"/><rect x=".5" y="2" width="17" height="3" fill="#fff"/><g fill="#7b8a93"><rect x="3" y="7" width="2" height="2"/><rect x="7" y="7" width="2" height="2"/><rect x="11" y="7" width="2" height="2"/><rect x="3" y="11" width="2" height="2"/><rect x="7" y="11" width="2" height="2"/><rect x="11" y="11" width="2" height="2"/></g></svg>
      </div>
      <table>
        <tr><th>M</th><th>T</th><th>W</th><th>T</th><th>F</th><th>S</th><th>S</th></tr>
        <tr><td></td><td></td><td></td><td>1</td><td>2</td><td>3</td><td>4</td></tr>
        <tr><td>5</td><td>6</td><td>7</td><td>8</td><td>9</td><td>10</td><td>11</td></tr>
        <tr><td>12</td><td>13</td><td class="today"><span>14</span></td><td>15</td><td>16</td><td>17</td><td>18</td></tr>
        <tr><td>19</td><td>20</td><td>21</td><td>22</td><td>23</td><td>24</td><td>25</td></tr>
        <tr><td>26</td><td>27</td><td>28</td><td>29</td><td>30</td><td>31</td><td></td></tr>
      </table>
    </div>
  </section>

  <footer class="footer">
    <div class="brand"><span class="brand-dot"></span><span class="brand-name">CORAL WIND STAYS</span></div>
    <div class="footer-links">
      Home<span class="sep">/</span>Corallo Holiday Home<span class="sep">/</span>Local Area<span class="sep">/</span>Book Now<span class="sep">/</span>Prices<span class="sep">/</span>Testimonials<span class="sep">/</span>Contact us<br>
      All right reserved copyright © 2013
    </div>
    <div class="footer-rule"></div>
    <nav class="social social-foot" aria-label="Social links">
      <a href="#"><span class="mark"></span></a>
      <a href="#"><span class="mark"></span></a>
      <a href="#"><span class="mark"></span></a>
      <a href="#"><svg width="12" height="9" viewBox="0 0 12 9"><rect x=".5" y=".5" width="11" height="8" fill="none" stroke="#fff"/><path d="M.5 .5 6 5 11.5 .5" fill="none" stroke="#fff"/></svg></a>
    </nav>
  </footer>
</div>
</body>
</html>
```